Modern labels for Murlane products

We need a new design of our labels for the product “Murlane” (https://www.murlane-example.eu/#) . The reason why we want to change our labels is to get a modern and more advanced look of our product. We also want to create a unique product that is attractive for our customers, even if the product are used in hospitals and healthcare centers for collecting dangerous waste.

There is three sizes of labels (55x95, 90x95, 170x95 mm) for different boxes, but the label will contain similar information. There are certain requirements and factors from regulations/standards that you need to follow when you create the new layout. But it’s up to you to change the design. You can work with background, fonts, effects, colors, structure, pattern, new symbols, logotype etc. The label could be any color, but the container will stay yellow so they have to look good together.

Keywords: Elegant, modern, functional, attractive, exclusive

Target Market(s)

Hospitals and healthcare centers

Industry/Entity Type

Product

Font styles to use
Serif
Sans Serif

Colors

Designer to choose colors to be used in the design.

Requirements
Must have
• Requirements for the regulations ADR UN3291 and ISO 23907 (PDF).
• * Symbol for danger waste
• * Filling level
• * "Danger"
• * Symbol for no second use
• * Symbol for manufaturer
• * Referencenumber
• * Text "”Clinical waste, Unspecified, N.O.S.”"
• * Area for series, certification, size and useful capacity
• * Area for Illustrations.
• * Text “Autoclavable at 134 c”, “Do not force closure” and “Do not overfill”.
• * Text for certification ”UN 3291 1H2/Y0,3/S/YR/N/QVK7148B”
• Three different sizes (55x95, 90x95, 170x95).
• More info in PDF "3kravspecifikation"
Nice to have
• A modern, elegant, advanced look of our label.
Should not have
• The information must be clear and readable, not too decorative/handwriting fonts.

```html
<!DOCTYPE html>
<html lang="en">
<head>
<meta charset="utf-8">
<title>Murlane clinical waste labels</title>
<link rel="stylesheet" href="https://fonts.googleapis.com/css2?family=Anton&family=Roboto+Condensed:wght@300;400;700&display=swap">
<style>
:root{
  --container-yellow:#fcdd1f;
  --label-black:#07090d;
  --paper:#ffffff;
  --danger-red:#e5232c;
  --illus-grey:#e6e6e6;
  --rule-grey:#c9c9c9;
}
*{margin:0;padding:0;box-sizing:border-box}
html,body{width:1003px;height:1200px;overflow:hidden;background:var(--container-yellow)}
body{position:relative;font-family:"Roboto Condensed",Arial,sans-serif;color:var(--paper)}
.label{position:absolute;background:var(--label-black)}
.label > *{position:absolute}
.label-large{left:110px;top:126px;width:784px;height:438px}
.label-medium{left:110px;top:608px;width:439px;height:415px}
.label-narrow{left:641px;top:608px;width:254px;height:438px}

.filling-level{display:flex;align-items:center;gap:14px}
.filling-level .arrow{flex:1;height:20px}
.filling-level span{letter-spacing:.55em;font-weight:400;white-space:nowrap}

.illustrations{background:var(--illus-grey);border-radius:6px;border:2px solid var(--paper)}
.waste-title{font-weight:700;text-transform:uppercase;line-height:.9;letter-spacing:-.01em}
.un-number{font-weight:700;line-height:1;letter-spacing:-.02em}
.packaging-code{font-weight:400;display:flex;align-items:center;gap:4px;white-space:nowrap}
.packaging-code svg{flex:none}
.danger{font-family:"Anton",Impact,sans-serif;color:var(--danger-red);line-height:1;letter-spacing:.01em}
.reference{font-weight:300;letter-spacing:.04em}

.maker{display:flex;flex-direction:column}
.maker-name{font-weight:700;line-height:1}
.maker-info{display:flex;align-items:flex-end;gap:5px;line-height:1.2;font-weight:400}

.record{background:var(--paper);color:var(--label-black);border-radius:4px;display:flex;flex-direction:column}
.record div{flex:1;display:flex;align-items:center;border-bottom:1px solid var(--rule-grey)}
.record div:last-child{border-bottom:none}

.spec-bar{background:var(--paper);color:var(--label-black);display:flex;flex-direction:column;justify-content:center}
.spec-bar p{display:flex;justify-content:space-between;white-space:nowrap;line-height:1.15}
.spec-bar .warn{font-weight:300}
.spec-bar .spec{font-weight:300}
.spec-bar b{font-weight:700}

.spec-vertical{background:var(--paper);color:var(--label-black)}
.spec-vertical .rot{position:absolute;left:50%;top:50%;width:318px;transform:translate(-50%,-50%) rotate(-90deg);font-size:8.2px;line-height:1.3}
.spec-vertical p{display:flex;justify-content:space-between;white-space:nowrap}
.spec-vertical b{font-weight:700}
</style>
</head>
<body>

<!-- 170 x 95 label -->
<section class="label label-large">
  <div class="filling-level" style="left:22px;top:20px;width:740px;font-size:18px">
    <svg class="arrow" viewBox="0 0 100 20" preserveAspectRatio="none"><path d="M1 10H100M10 2L1 10L10 18" fill="none" stroke="#fff" stroke-width="1.6" vector-effect="non-scaling-stroke"/></svg>
    <span>FILLING LEVEL</span>
    <svg class="arrow" viewBox="0 0 100 20" preserveAspectRatio="none"><path d="M0 10H99M90 2L99 10L90 18" fill="none" stroke="#fff" stroke-width="1.6" vector-effect="non-scaling-stroke"/></svg>
  </div>
  <div class="illustrations" role="img" aria-label="Step-by-step drawings: opening the box, inserting sharps, temporary and final closure" style="left:22px;top:59px;width:262px;height:226px"></div>
  <h2 class="waste-title" style="left:306px;top:60px;font-size:43px">Clinical waste,<br>unspecified,<br>N.O.S.</h2>
  <div class="un-number" style="left:304px;top:188px;font-size:58px">UN3291</div>
  <div class="packaging-code" style="left:308px;top:240px;font-size:13px">
    <svg width="13" height="13" viewBox="0 0 20 20"><circle cx="10" cy="10" r="8.5" fill="none" stroke="#fff" stroke-width="1.6"/><path d="M7 5v10M13 5v10M7 10h6" stroke="#fff" stroke-width="1.6"/></svg>
    1H2/Y0.3/S/YR/N/QVK7148B
  </div>
  <svg style="left:573px;top:72px;width:184px;height:184px" viewBox="0 0 200 200" role="img" aria-label="Class 6.2 infectious substance hazard label">
    <polygon points="100,2 198,100 100,198 2,100" fill="#fff"/>
    <polygon points="100,11 189,100 100,189 11,100" fill="none" stroke="#07090d" stroke-width="3"/>
    <g fill="none" stroke="#07090d" stroke-width="7">
      <circle cx="100" cy="62" r="19"/><circle cx="79" cy="96" r="19"/><circle cx="121" cy="96" r="19"/>
      <circle cx="100" cy="84" r="24" stroke-width="4"/>
    </g>
    <circle cx="100" cy="84" r="6" fill="#07090d"/>
    <text x="100" y="178" text-anchor="middle" font-family="Roboto Condensed,sans-serif" font-size="20" fill="#07090d">6</text>
  </svg>
  <svg style="left:714px;top:58px;width:53px;height:53px" viewBox="0 0 60 60" role="img" aria-label="Do not reuse">
    <circle cx="30" cy="30" r="27" fill="none" stroke="#fff" stroke-width="3"/>
    <text x="30" y="43" text-anchor="middle" font-family="Roboto Condensed,sans-serif" font-size="38" fill="#fff">2</text>
    <path d="M11 49L49 11" stroke="#fff" stroke-width="3"/>
  </svg>
  <div class="danger" style="left:22px;top:296px;font-size:33px">DANGER</div>
  <div class="reference" style="left:22px;top:340px;font-size:13px">XXXXX-XX-XX-XX</div>
  <div class="maker" style="left:154px;top:296px">
    <div class="maker-name" style="font-size:30px">Murlane</div>
    <div class="maker-info" style="font-size:12px;margin-top:4px">
      <svg width="27" height="22" viewBox="0 0 27 22"><path d="M0 22V9l6 4V9l6 4V9l6 4V0h5v22z" fill="#fff"/></svg>
      <span>Norrvik, Sweden<br>www.murlane-example.eu</span>
    </div>
  </div>
  <div class="record" style="left:325px;top:272px;width:438px;height:85px;font-size:13px">
    <div style="padding-left:12px">PLACE / CLINIC</div>
    <div style="padding-left:12px">DEPARTMENT</div>
    <div style="padding-left:12px">SEALED BY &amp; DATE</div>
  </div>
  <div class="spec-bar" style="left:22px;top:366px;width:740px;height:58px;padding:0 36px;font-size:21px">
    <p class="warn"><span>AUTOCLAVABLE AT 134 °C</span><span>DO NOT OVERFILL</span><span>DO NOT FORCE CLOSURE</span></p>
    <p class="spec"><span>Series: <b>Tarn</b></span><span>Certification: <b>ISO23907:2012</b></span><span>Size: <b>2,2 L</b></span><span>Useful capacity: <b>1,76 L</b></span></p>
  </div>
</section>

<!-- 90 x 95 label -->
<section class="label label-medium">
  <div class="filling-level" style="left:17px;top:16px;width:405px;font-size:15px;gap:10px">
    <svg class="arrow" viewBox="0 0 100 20" preserveAspectRatio="none"><path d="M1 10H100M10 2L1 10L10 18" fill="none" stroke="#fff" stroke-width="1.5" vector-effect="non-scaling-stroke"/></svg>
    <span>FILLING LEVEL</span>
    <svg class="arrow" viewBox="0 0 100 20" preserveAspectRatio="none"><path d="M0 10H99M90 2L99 10L90 18" fill="none" stroke="#fff" stroke-width="1.5" vector-effect="non-scaling-stroke"/></svg>
  </div>
  <div class="illustrations" role="img" aria-label="Step-by-step drawings: opening the box, inserting sharps, temporary and final closure" style="left:12px;top:59px;width:210px;height:181px"></div>
  <h2 class="waste-title" style="left:233px;top:58px;font-size:27.5px">Clinical waste,<br>unspecified,<br>N.O.S.</h2>
  <div class="un-number" style="left:10px;top:248px;font-size:42px">UN3291</div>
  <div class="packaging-code" style="left:13px;top:288px;font-size:10px">
    <svg width="11" height="11" viewBox="0 0 20 20"><circle cx="10" cy="10" r="8.5" fill="none" stroke="#fff" stroke-width="1.8"/><path d="M7 5v10M13 5v10M7 10h6" stroke="#fff" stroke-width="1.8"/></svg>
    1H2/Y0.3/S/YR/N/QVK7148B
  </div>
  <svg style="left:287px;top:131px;width:134px;height:134px" viewBox="0 0 200 200" role="img" aria-label="Class 6.2 infectious substance hazard label">
    <polygon points="100,2 198,100 100,198 2,100" fill="#fff"/>
    <polygon points="100,11 189,100 100,189 11,100" fill="none" stroke="#07090d" stroke-width="3"/>
    <g fill="none" stroke="#07090d" stroke-width="7">
      <circle cx="100" cy="62" r="19"/><circle cx="79" cy="96" r="19"/><circle cx="121" cy="96" r="19"/>
      <circle cx="100" cy="84" r="24" stroke-width="4"/>
    </g>
    <circle cx="100" cy="84" r="6" fill="#07090d"/>
    <text x="100" y="178" text-anchor="middle" font-family="Roboto Condensed,sans-serif" font-size="20" fill="#07090d">6</text>
  </svg>
  <svg style="left:388px;top:119px;width:38px;height:38px" viewBox="0 0 60 60" role="img" aria-label="Do not reuse">
    <circle cx="30" cy="30" r="27" fill="none" stroke="#fff" stroke-width="3"/>
    <text x="30" y="43" text-anchor="middle" font-family="Roboto Condensed,sans-serif" font-size="38" fill="#fff">2</text>
    <path d="M11 49L49 11" stroke="#fff" stroke-width="3"/>
  </svg>
  <div class="danger" style="left:173px;top:252px;font-size:34px">DANGER</div>
  <div class="reference" style="left:175px;top:291px;font-size:12px">XXXXX-XX-XX-XX</div>
  <div class="maker" style="left:10px;top:306px">
    <div class="maker-name" style="font-size:24px">Murlane</div>
    <div class="maker-info" style="font-size:10px;margin-top:3px">
      <svg width="22" height="18" viewBox="0 0 27 22"><path d="M0 22V9l6 4V9l6 4V9l6 4V0h5v22z" fill="#fff"/></svg>
      <span>Norrvik, Sweden<br>www.murlane-example.eu</span>
    </div>
  </div>
  <div class="record" style="left:145px;top:304px;width:282px;height:54px;font-size:9.5px">
    <div style="padding-left:8px">PLACE / CLINIC</div>
    <div style="padding-left:8px">DEPARTMENT</div>
    <div style="padding-left:8px">SEALED BY &amp; DATE</div>
  </div>
  <div class="spec-bar" style="left:12px;top:368px;width:414px;height:33px;padding:0 20px;font-size:11.5px">
    <p class="warn"><span>AUTOCLAVABLE AT 134 °C</span><span>DO NOT OVERFILL</span><span>DO NOT FORCE CLOSURE</span></p>
    <p class="spec"><span>Series: <b>Tarn</b></span><span>Certification: <b>ISO23907:2012</b></span><span>Size: <b>2,2 L</b></span><span>Useful capacity: <b>1,76 L</b></span></p>
  </div>
</section>

<!-- 55 x 95 label -->
<section class="label label-narrow">
  <div class="filling-level" style="left:11px;top:9px;width:232px;font-size:10px;gap:6px">
    <svg class="arrow" viewBox="0 0 100 20" preserveAspectRatio="none"><path d="M1 10H100M10 2L1 10L10 18" fill="none" stroke="#fff" stroke-width="1.2" vector-effect="non-scaling-stroke"/></svg>
    <span>FILLING LEVEL</span>
    <svg class="arrow" viewBox="0 0 100 20" preserveAspectRatio="none"><path d="M0 10H99M90 2L99 10L90 18" fill="none" stroke="#fff" stroke-width="1.2" vector-effect="non-scaling-stroke"/></svg>
  </div>
  <div class="illustrations" role="img" aria-label="Step-by-step drawings: opening the box, inserting sharps, temporary and final closure" style="left:12px;top:41px;width:186px;height:161px"></div>
  <div class="spec-vertical" style="left:217px;top:40px;width:26px;height:324px">
    <div class="rot">
      <p style="font-weight:300"><span>AUTOCLAVABLE AT 134 °C</span><span>DO NOT OVERFILL</span><span>DO NOT FORCE CLOSURE</span></p>
      <p style="font-weight:300"><span>Series: <b>Tarn</b></span><span>Certification: <b>ISO23907:2012</b></span><span>Size: <b>2,2 L</b></span><span>Useful capacity: <b>1,76 L</b></span></p>
    </div>
  </div>
  <h2 class="waste-title" style="left:11px;top:210px;font-size:22.5px">Clinical waste,<br>unspecified,<br>N.O.S.</h2>
  <div class="un-number" style="left:11px;top:292px;font-size:28px">UN3291</div>
  <div class="packaging-code" style="left:12px;top:320px;font-size:7px;gap:2px">
    <svg width="8" height="8" viewBox="0 0 20 20"><circle cx="10" cy="10" r="8.5" fill="none" stroke="#fff" stroke-width="2"/><path d="M7 5v10M13 5v10M7 10h6" stroke="#fff" stroke-width="2"/></svg>
    1H2/Y0.3/S/YR/N/QVK7148B
  </div>
  <svg style="left:117px;top:248px;width:96px;height:96px" viewBox="0 0 200 200" role="img" aria-label="Class 6.2 infectious substance hazard label">
    <polygon points="100,2 198,100 100,198 2,100" fill="#fff"/>
    <polygon points="100,11 189,100 100,189 11,100" fill="none" stroke="#07090d" stroke-width="3"/>
    <g fill="none" stroke="#07090d" stroke-width="7">
      <circle cx="100" cy="62" r="19"/><circle cx="79" cy="96" r="19"/><circle cx="121" cy="96" r="19"/>
      <circle cx="100" cy="84" r="24" stroke-width="4"/>
    </g>
    <circle cx="100" cy="84" r="6" fill="#07090d"/>
    <text x="100" y="178" text-anchor="middle" font-family="Roboto Condensed,sans-serif" font-size="20" fill="#07090d">6</text>
  </svg>
  <svg style="left:181px;top:243px;width:27px;height:27px" viewBox="0 0 60 60" role="img" aria-label="Do not reuse">
    <circle cx="30" cy="30" r="27" fill="none" stroke="#fff" stroke-width="3.5"/>
    <text x="30" y="43" text-anchor="middle" font-family="Roboto Condensed,sans-serif" font-size="38" fill="#fff">2</text>
    <path d="M11 49L49 11" stroke="#fff" stroke-width="3.5"/>
  </svg>
  <div class="maker" style="left:11px;top:350px">
    <div class="maker-name" style="font-size:16px">Murlane</div>
    <div class="maker-info" style="font-size:6px;margin-top:1px;gap:3px">
      <svg width="14" height="11" viewBox="0 0 27 22"><path d="M0 22V9l6 4V9l6 4V9l6 4V0h5v22z" fill="#fff"/></svg>
      <span>Norrvik, Sweden<br>www.murlane-example.eu</span>
    </div>
  </div>
  <div class="danger" style="left:97px;top:358px;font-size:22px">DANGER</div>
  <div class="reference" style="left:180px;top:370px;font-size:8px">XXXXX-XX-XX-XX</div>
  <div class="record" style="left:11px;top:384px;width:232px;height:44px;font-size:7px">
    <div style="padding-left:6px">PLACE / CLINIC</div>
    <div style="padding-left:6px">DEPARTMENT</div>
    <div style="padding-left:6px">SEALED BY &amp; DATE</div>
  </div>
</section>

</body>
</html>
```